Design Brief: Brand, Business Card and Basic Corp ID for Tandem. Accounting and Tax

Background:
Tandem Accounting and Tax has been established in 2012 in Sydney Australia. Tandem is now at the stage of the business where it needs a strong brand look and feel so that we can start promoting the business to new clients.
Tandem is run by a young accountant who has previously owned a successful accounting practice. The look and feel of the previous business (franchised) was heavily corporate and projected a professional, but dated feel.
Desired Tone:
Young, urban, professional and forward thinking accountants. It’s the accountant for the young professional.
Look & Feel
Please see below image for the style Tandem Accounting and Tax are looking for in their brand execution. It needs to be a clean type logo with either a slab serif or serif as the hero font. There should be a good use of white space with design consideration taken of the kerning between the lettering. A sans-serif font can be used as a secondary font to compliment the Tandem logo. Please note, no image is needed to compliment the logo, it is strictly typographic.
In terms of colours, Tandem still needs to be professional and so black or a strong grey will be the hero colour(s), however Tandem will be open to other secondary colour pallets to accompany it.
Requirements
Rather than see a logo, we would like to see a design execution on a business card as we already have a clear understanding of what we would like the logo to look like.
1. Business Card:
Print Specs: The business card will be 90mmW x 55mmH, Letterpress printed on a 600gsm Falcon Velina. As the business card will be letterpress printed please use only one PMS colour (maximum of two) No files with CMYK.
- Tandem Logo on the front and center (please note the ‘stop’ after tandem. Tandem can be in lower case, upper case or sentence case.
- Details on the reverse as follows:
Accounting and Tax
Luke Harwood, Director
+ 61 455 372 916
luke@tandemexample.com.au
PO Box 2874, Randwick
2. Letterhead
Print Specs:
A4 (297mmH x 210mmW) single sided
As per the business card, logo and details aligned in top left hand corner
3. With compliments slip
Print Specs:
99mmH x 210mmW, Glued along short left edge in pads of 50 (so please allow 5 - 10mm from edge), single sided. Can be prepared in CMYK.
Design should be as per the business card, but on one side.
Logo file types:
Please supply business card as open artwork, either packaged indesign or illustrator files (Not photoshop) Please ensure all fonts are embedded and that the font has been noted so we are able to purchase later.
Please supply the letterhead as a word doc and the with compliments slip as either packaged indesign or illustrator files (not photoshop please).
Industry/Entity Type
Accounting
Logo Text
tandem.
Logo styles of interest
Wordmark Logo
Look and feel
Each slider illustrates characteristics of the customer's brand and the style your logo design should communicate.

```html
<!DOCTYPE html>
<html lang="en">
<head>
<meta charset="utf-8">
<title>Tandem. Accounting and Tax — Stationery</title>
<link rel="stylesheet" href="https://fonts.googleapis.com/css2?family=Playfair+Display:wght@500&family=Arimo:wght@400;700&display=swap">
<style>
  :root {
    --ink: #0a0a0a;
    --paper: #ffffff;
    --canvas: #f4f4f4;
    --edge: #d6d6d6;
  }
  * { margin: 0; padding: 0; box-sizing: border-box; }
  html, body { width: 1200px; height: 1000px; overflow: hidden; }
  body {
    position: relative;
    background: var(--canvas);
    color: var(--ink);
    font-family: "Arimo", Arial, sans-serif;
  }
  .wordmark {
    font-family: "Playfair Display", Georgia, serif;
    font-weight: 500;
    letter-spacing: -0.03em;
    line-height: 1;
    color: var(--ink);
    white-space: nowrap;
  }
  .tagline {
    font-family: "Arimo", Arial, sans-serif;
    font-weight: 400;
    color: var(--ink);
    white-space: nowrap;
  }
  .lockup { position: absolute; }
  .lockup--hero { left: 52px; top: 490px; }
  .lockup--hero .wordmark { font-size: 104px; }
  .lockup--stacked { left: 52px; top: 672px; }
  .lockup--stacked .wordmark { font-size: 104px; }
  .lockup--stacked .tagline { font-size: 22px; margin: -6px 0 0 66px; }

  .sheet {
    position: absolute;
    background: var(--paper);
    border: 1px solid var(--edge);
    overflow: hidden;
  }
  .sheet__band {
    position: absolute; left: 0; right: 0; bottom: 0;
    background: var(--ink);
  }
  .mini-lockup { position: absolute; }
  .mini-lockup .wordmark { font-size: 30px; }
  .mini-lockup .tagline { font-size: 7px; margin: -2px 0 0 16px; }

  .rules { position: absolute; display: flex; flex-direction: column; gap: 6px; }
  .rules span { display: block; height: 2.5px; background: var(--ink); }

  .letterhead { left: 445px; top: 100px; width: 545px; height: 790px; }
  .letterhead .sheet__band { height: 10px; }
  .letterhead .mini-lockup { left: 34px; top: 56px; }
  .letterhead .rules { left: 36px; top: 104px; }

  .card-front { left: 878px; top: 167px; width: 246px; height: 150px; }
  .card-front .wordmark {
    position: absolute; left: 0; right: 0; top: 52px;
    text-align: center; font-size: 44px;
  }

  .card-back { left: 876px; top: 339px; width: 246px; height: 150px; }
  .card-back .mini-lockup { left: 20px; top: 12px; }
  .card-back .name {
    position: absolute; left: 22px; top: 80px;
    font-size: 9px; font-weight: 700; letter-spacing: -0.02em;
  }
  .card-back .rules { left: 22px; top: 92px; gap: 5px; }
  .card-back .rules span { height: 2px; }

  .compliments { left: 625px; top: 547px; width: 550px; height: 258px; }
  .compliments .sheet__band { height: 14px; }
  .compliments .mini-lockup { left: 28px; top: 24px; }
  .compliments .rules { left: 30px; top: 72px; }
</style>
</head>
<body>

  <div class="lockup lockup--hero">
    <div class="wordmark">tandem.</div>
  </div>

  <div class="lockup lockup--stacked">
    <div class="wordmark">tandem.</div>
    <div class="tagline">Accounting and Tax</div>
  </div>

  <section class="sheet letterhead" aria-label="Letterhead">
    <div class="mini-lockup">
      <div class="wordmark">tandem.</div>
      <div class="tagline">Accounting and Tax</div>
    </div>
    <div class="rules">
      <span style="width:56px"></span>
      <span style="width:86px"></span>
      <span style="width:76px"></span>
    </div>
    <div class="sheet__band"></div>
  </section>

  <section class="sheet card-front" aria-label="Business card front">
    <div class="wordmark">tandem.</div>
  </section>

  <section class="sheet card-back" aria-label="Business card back">
    <div class="mini-lockup">
      <div class="wordmark">tandem.</div>
      <div class="tagline">Accounting and Tax</div>
    </div>
    <div class="name">Luke Harwood</div>
    <div class="rules">
      <span style="width:56px"></span>
      <span style="width:86px"></span>
      <span style="width:76px"></span>
    </div>
  </section>

  <section class="sheet compliments" aria-label="With compliments slip">
    <div class="mini-lockup">
      <div class="wordmark">tandem.</div>
      <div class="tagline">Accounting and Tax</div>
    </div>
    <div class="rules">
      <span style="width:56px"></span>
      <span style="width:86px"></span>
      <span style="width:76px"></span>
    </div>
    <div class="sheet__band"></div>
  </section>

</body>
</html>
```